Bitcoin Casino User Interface

This is a responsive design for a new bitcoin casino called the brass latch casino

The 4 games I need the Ui for are video poker, blackjack, roulette and dice

The designs should be ideal for mobile and have a bit of a retro feel

Good example is www.plumreelhallvexcom

Target Market(s)

Adults between the ages of 21-55 all over the world

Industry/Entity Type

Casino

Font styles to use
Serif

Colors
5dc4b5
ffffff

Requirements
Must have
• Must be responsive and look great on mobile
design must be functional
Should not have
• Any generic and standard elements

```html
<!DOCTYPE html>
<html lang="en">
<head>
<meta charset="utf-8">
<title>Brass Latch Casino – Blackjack</title>
<link href="https://fonts.googleapis.com/css2?family=Poiret+One&family=Oswald:wght@400;500&family=Open+Sans:wght@400;600&display=swap" rel="stylesheet">
<style>
:root{
  --page:#6aa3a2;
  --header:#74b9b6;
  --nav:#5e9c9a;
  --ribbon:#4f8785;
  --white:#ffffff;
  --felt:#1f6b34;
  --felt-dark:#175a2a;
  --felt-head:#2f9a4a;
  --pay-green:#5ce88a;
  --dont:#8a2520;
  --gold:#f0a81a;
  --gold-text:#f2d340;
  --grey-btn:#b5b5b5;
  --grey-text:#6a6a6a;
  --green-btn:#2fbf5a;
  --chat-bg:#555050;
  --chat-tab:#5e9c9a;
  --users-tab:#a9a6a6;
  --chat-text:#e8e8e8;
  --chat-green:#5ce88a;
  --chat-red:#f06060;
  --table-bg:#6aa9a6;
  --table-alt:#5e9c9a;
  --table-head:#5a9693;
  --footer-text:#444;
  --red-suit:#e03030;
}
*{margin:0;padding:0;box-sizing:border-box}
html,body{width:955px;height:1200px;overflow:hidden;background:var(--page);font-family:"Open Sans",sans-serif}
.canvas{position:relative;width:955px;height:1200px}
.abs{position:absolute}

.ribbon-tail{top:100px;width:60px;height:40px;background:var(--ribbon)}
.ribbon-tail.left{left:82px;clip-path:polygon(0 0,100% 0,100% 100%,0 100%,22% 50%)}
.ribbon-tail.right{left:822px;clip-path:polygon(0 0,100% 0,78% 50%,100% 100%,0 100%)}

.site-header{left:114px;top:0;width:736px;height:90px;background:var(--header)}
.brand{position:absolute;left:0;right:0;top:14px;text-align:center;font-family:"Poiret One",sans-serif;font-size:52px;color:var(--white);letter-spacing:2px;line-height:60px}
.brand-dot{display:inline-block;width:38px;height:38px;border-radius:50%;background:var(--white);opacity:.85;vertical-align:-4px;margin-right:14px}
.main-nav{left:114px;top:90px;width:736px;height:40px;background:var(--nav);display:flex;justify-content:center;gap:44px;align-items:center}
.main-nav a{font-family:"Oswald",sans-serif;font-size:23px;color:var(--white);text-decoration:none;letter-spacing:1px}
.main-nav a.active{color:#4b4b4b}

.sheet{left:114px;top:130px;width:736px;height:974px;background:var(--white);box-shadow:0 2px 8px rgba(0,0,0,.25)}

.game{left:132px;top:149px;width:520px;height:559px;background:var(--felt)}
.game-title{height:37px;background:linear-gradient(var(--felt-head),#238a3e);color:var(--white);font-family:"Oswald",sans-serif;font-size:16px;text-align:center;line-height:37px;letter-spacing:.5px}
.paytable{position:absolute;top:37px;left:0;width:376px;height:98px;background:var(--felt-dark);border-bottom:1px solid #2e8044;font-size:10.5px;font-weight:600;color:var(--white)}
.paytable span{position:absolute}
.paytable .val{color:var(--pay-green)}
.side-btn{position:absolute;left:376px;width:144px;font-family:"Oswald",sans-serif;color:var(--gold-text);text-align:center;font-size:15px}
.side-btn.dont{top:37px;height:40px;line-height:40px;background:var(--dont)}
.side-btn.play{top:77px;height:58px;background:var(--felt-dark);border-left:1px solid #2e8044;border-bottom:1px solid #2e8044;padding-top:10px;line-height:19px}

.card{position:absolute;width:91px;height:129px;background:var(--white);border-radius:5px;box-shadow:0 1px 3px rgba(0,0,0,.4);font-family:"Open Sans",sans-serif}
.card .idx{position:absolute;left:5px;top:3px;font-size:15px;font-weight:600;line-height:15px}
.card .idx.bottom{left:auto;right:5px;top:auto;bottom:3px;transform:rotate(180deg)}
.card.black{color:#111}
.card.red{color:var(--red-suit)}
.pips{position:absolute;left:18px;top:14px;width:55px;height:101px;display:grid;grid-template-columns:1fr 1fr;align-items:center;justify-items:center;font-size:20px;line-height:20px}
.figure{position:absolute;left:18px;top:12px;width:55px;height:105px;border-radius:3px}
.figure.king{background:linear-gradient(#c9c9c9,#d94a2a 50%,#3a3a3a)}
.figure.queen{background:linear-gradient(#e8c060,#e07a30 55%,#f0d070)}

.bet{position:absolute;top:459px;left:0;width:520px;height:30px}
.bet .label{position:absolute;left:238px;font-family:"Oswald",sans-serif;font-size:21px;color:var(--white)}
.bet .credits{position:absolute;right:12px;font-family:"Oswald",sans-serif;font-size:21px;color:var(--gold)}
.controls button{position:absolute;top:503px;height:38px;border:none;border-radius:2px;font-family:"Oswald",sans-serif;font-size:15px;letter-spacing:.5px;box-shadow:inset 0 -3px 0 rgba(0,0,0,.18)}
.btn-gold{background:var(--gold);color:var(--white)}
.btn-grey{background:var(--grey-btn);color:var(--grey-text)}
.btn-green{background:var(--green-btn);color:var(--white)}

.chat{left:670px;top:149px;width:160px;height:355px;background:var(--chat-bg)}
.chat-tabs{display:flex;height:37px;font-family:"Oswald",sans-serif;font-size:16px;color:var(--white)}
.chat-tabs div{flex:1;text-align:center;line-height:37px}
.chat-tabs .on{background:var(--chat-tab)}
.chat-tabs .off{background:var(--users-tab)}
.chat-log{padding:7px 8px;font-size:10.4px;line-height:12.6px;color:var(--chat-text)}
.chat-log p{margin-bottom:12px}
.chat-log p.tight{margin-bottom:0}
.chat-log .muted{color:#bbb}
.chat-log .joined{color:var(--chat-green)}
.chat-log .left{color:var(--chat-red)}

.history{left:132px;top:725px;width:698px;height:289px;background:var(--table-bg)}
.history-tabs{height:39px;background:var(--table-head);display:flex;justify-content:center;gap:0;font-family:"Oswald",sans-serif;font-size:15px;color:var(--white)}
.history-tabs div{padding:0 14px;line-height:39px}
.history-tabs .on{background:var(--table-bg);color:#3c3c3c;margin-top:4px;line-height:35px}
.history table{width:100%;border-collapse:collapse;font-size:10.5px;color:var(--white)}
.history th{height:34px;text-align:left;font-weight:400;padding-top:4px}
.history td{height:26.3px}
.history th:first-child,.history td:first-child{padding-left:12px}
.history tbody tr:nth-child(odd){background:var(--table-alt)}
.history .user{color:#3a5a58;text-decoration:underline}
.history .mult{color:#2f5250}

.site-footer{left:114px;top:1043px;width:736px;text-align:center;font-size:14px;color:var(--footer-text)}
.site-footer span{margin:0 14px}
</style>
</head>
<body>
<div class="canvas">
  <div class="abs ribbon-tail left"></div>
  <div class="abs ribbon-tail right"></div>

  <header class="abs site-header">
    <div class="brand"><span class="brand-dot"></span>BRASS LATCH CASINO</div>
  </header>
  <nav class="abs main-nav">
    <a href="#">VIDEO POKER</a>
    <a href="#" class="active">BLACKJACK</a>
    <a href="#">ROULETTE</a>
    <a href="#">DICE</a>
  </nav>

  <main class="abs sheet"></main>

  <section class="abs game">
    <div class="game-title">LUCKY 7'S PROGRESSIVE BLACKJACK</div>
    <div class="paytable">
      <span style="left:12px;top:13px">THREE 7's</span><span class="val" style="left:120px;top:13px">77,516.80</span>
      <span style="left:12px;top:42px">THREE 7's SUITED</span><span class="val" style="left:120px;top:42px">1000</span>
      <span style="left:12px;top:71px">THREE 7's</span><span class="val" style="left:120px;top:71px">250</span>
      <span style="left:204px;top:13px">FIRST TWO 7's SUITED</span><span class="val" style="left:332px;top:13px">50</span>
      <span style="left:204px;top:42px">FIRST TWO 7's</span><span class="val" style="left:332px;top:42px">1000</span>
      <span style="left:204px;top:71px">FIRST CARD 7</span><span class="val" style="left:332px;top:71px">250</span>
    </div>
    <div class="side-btn dont">DONT PLAY</div>
    <div class="side-btn play">PLAY LUCKY 7'S<br>1 CREDIT</div>

    <div class="card black" style="left:166px;top:158px">
      <span class="idx">10</span>
      <div class="pips"><span>♣</span><span>♣</span><span>♣</span><span>♣</span><span>♣</span><span>♣</span><span>♣</span><span>♣</span><span>♣</span><span>♣</span></div>
      <span class="idx bottom">10</span>
    </div>
    <div class="card black" style="left:264px;top:158px">
      <span class="idx">K</span>
      <div class="figure king" role="img" aria-label="King of clubs court figure"></div>
      <span class="idx bottom">K</span>
    </div>
    <div class="card red" style="left:166px;top:305px">
      <span class="idx">Q</span>
      <div class="figure queen" role="img" aria-label="Queen of diamonds court figure"></div>
      <span class="idx bottom">Q</span>
    </div>
    <div class="card red" style="left:264px;top:305px">
      <span class="idx">9</span>
      <div class="pips"><span>♥</span><span>♥</span><span>♥</span><span>♥</span><span>♥</span><span>♥</span><span>♥</span><span>♥</span><span style="grid-column:1 / span 2">♥</span></div>
      <span class="idx bottom">9</span>
    </div>

    <div class="bet"><span class="label">BET 1</span><span class="credits">1000 CREDITS</span></div>
    <div class="controls">
      <button class="btn-gold" style="left:12px;width:56px">AUTO</button>
      <button class="btn-grey" style="left:76px;width:64px">DOUBLE</button>
      <button class="btn-grey" style="left:148px;width:62px">SPLIT</button>
      <button class="btn-green" style="left:218px;width:84px">CHANGE BET</button>
      <button class="btn-grey" style="left:310px;width:62px">HIT</button>
      <button class="btn-grey" style="left:380px;width:64px">STAND</button>
      <button class="btn-gold" style="left:451px;width:57px">DRAW</button>
    </div>
  </section>

  <aside class="abs chat">
    <div class="chat-tabs"><div class="on">CHAT</div><div class="off">USERS</div></div>
    <div class="chat-log">
      <p>* Welcome to Plumreel Hall - Video Poker!<br>[08/31/2014 3:32pm]</p>
      <p class="joined">* 781afc57db has joined.</p>
      <p><span class="muted">* 781afc57db:</span><br>We have added 2 factor authentication and password protection for accounts.<br>[08/31/2014 3:32pm]</p>
      <p class="tight joined">* ZeroSum has joined.</p>
      <p class="tight left">* 781afc57db has left.</p>
      <p class="tight joined">* 84b7c04782 has joined.</p>
    </div>
  </aside>

  <section class="abs history">
    <div class="history-tabs"><div>RECENT</div><div class="on">MY GAMES</div><div>BIG WINS</div><div>RARE WINS</div><div>LEADERBOARD</div><div>ACCOUNT</div></div>
    <table>
      <thead><tr><th style="width:163px">Date</th><th style="width:107px">User</th><th style="width:108px">Game</th><th style="width:86px">BTC Bet</th><th style="width:107px">Result</th><th>BTC Payment</th></tr></thead>
      <tbody>
        <tr><td>Aug 31, 2014 at 6:48pm</td><td class="user">bd9cf71835</td><td>Jacks or Better</td><td>0.0256</td><td>Win &lt; 49.5000</td><td>0.0004 <span class="mult">(win 2X)</span></td></tr>
        <tr><td>Aug 31, 2014 at 6:48pm</td><td class="user">bd9cf71835</td><td>Jacks or Better</td><td>0.0256</td><td>Win &lt; 49.5000</td><td>0.0004 <span class="mult">(win 2X)</span></td></tr>
        <tr><td>Aug 31, 2014 at 6:48pm</td><td class="user">bd9cf71835</td><td>Jacks or Better</td><td>0.0256</td><td>Win &lt; 49.5000</td><td>0.0004 <span class="mult">(win 2X)</span></td></tr>
        <tr><td>Aug 31, 2014 at 6:48pm</td><td class="user">bd9cf71835</td><td>Jacks or Better</td><td>0.0256</td><td>Win &lt; 49.5000</td><td>0.0004 <span class="mult">(win 2X)</span></td></tr>
        <tr><td>Aug 31, 2014 at 6:48pm</td><td class="user">bd9cf71835</td><td>Jacks or Better</td><td>0.0256</td><td>Win &lt; 49.5000</td><td>0.0004 <span class="mult">(win 2X)</span></td></tr>
        <tr><td>Aug 31, 2014 at 6:48pm</td><td class="user">bd9cf71835</td><td>Jacks or Better</td><td>0.0256</td><td>Win &lt; 49.5000</td><td>0.0004 <span class="mult">(win 2X)</span></td></tr>
        <tr><td>Aug 31, 2014 at 6:48pm</td><td class="user">bd9cf71835</td><td>Jacks or Better</td><td>0.0256</td><td>Win &lt; 49.5000</td><td>0.0004 <span class="mult">(win 2X)</span></td></tr>
        <tr><td>Aug 31, 2014 at 6:48pm</td><td class="user">bd9cf71835</td><td>Jacks or Better</td><td>0.0256</td><td>Win &lt; 49.5000</td><td>0.0004 <span class="mult">(win 2X)</span></td></tr>
      </tbody>
    </table>
  </section>

  <footer class="abs site-footer">
    <span>Terms of Service</span>|<span>Admin@brasslatchcasino.com</span>|<span>Ledgertalk Forum</span>
  </footer>
</div>
</body>
</html>
```